Polystyrene Environmental Synopsis

We need a fact sheet for quick reference that groups information units and has a simple but engaging visual presentation of the text and various infographics. We are a trade association representing polystyrene foam manufacturers and this piece is intended to help our members provide effective messaging to their sales personnel.

To view our typical company design/style please see our website at www.foamtradeunion.org. Our primary RGB colors are: (187,140,9); (94,47,29); (94,138,164); and (164,167,15). Secondary RGB colors are (249,162,28) and (218,210,208). Our title/header font is DIN Next LT Pro and our copy font is Calibri 10.5 pt. We can deviate from the font specification if beneficial.

Target Market(s)

Polystyrene manufacturer plant workers and other employees.

Font styles to use
Sans Serif

Requirements
Must have
• Information presentation must be clean and easy to reference.

```html
<!DOCTYPE html>
<html lang="en">
<head>
<meta charset="utf-8">
<title>Polystyrene Environmental Synopsis</title>
<link href="https://fonts.googleapis.com/css2?family=Source+Sans+3:wght@400;600;700&family=Barlow:wght@500;600;700&display=swap" rel="stylesheet">
<style>
:root{
  --gold:#bb8c09; --brown:#5e2f1d; --blue:#5e8aa4; --olive:#a4a70f;
  --orange:#f9a21c; --grey:#dad2d0; --clay:#a9735a; --ink:#2e2e2e;
  --stage:#ece8e4;
}
*{margin:0;padding:0;box-sizing:border-box}
html,body{width:1200px;height:787px;overflow:hidden;background:var(--stage)}
body{position:relative;font-family:"Source Sans 3",sans-serif;color:var(--ink)}
.page{position:absolute;width:678px;height:875px;background:#fff;transform:scale(.8);transform-origin:0 0;box-shadow:0 2px 8px rgba(0,0,0,.12)}
.page--talking{left:42px;top:30px}
.page--units{left:622px;top:26px}
.abs{position:absolute}
.doc-title{left:37px;top:12px;font:600 29px "Source Sans 3",sans-serif;color:var(--blue)}
.title-rule{left:277px;top:23px;width:365px;height:23px;background:var(--grey)}
.intro{left:37px;top:58px;width:603px;font-size:14.6px;line-height:19px;text-align:justify}
.section-head{left:37px;top:127px;font:600 18px "Source Sans 3",sans-serif;color:var(--olive)}
.copy{font-size:10px;line-height:15.5px;text-align:justify}
.copy b{font-size:13px;font-weight:600}
.unit-bar{left:36px;width:606px;height:24px;background:var(--grey);display:flex;align-items:center;justify-content:center;gap:8px}
.unit-bar small{font-size:9px}
.unit-bar span{font:500 15px "Barlow",sans-serif;letter-spacing:.5px;color:#333}
.frame{border-top:1px solid;border-left:1px solid}
.col-title{font:600 11.5px/16px "Source Sans 3",sans-serif;text-align:center;background:#fff;padding:0 6px}
.fine{font-size:7.8px;line-height:10px}
.fine em{font-style:normal;font-weight:700}
.big{font-weight:600;font-size:15px}
.flat{border-radius:3px}
.olive{color:var(--olive)} .blue{color:var(--blue)} .orange{color:var(--orange)}
.gold{color:var(--gold)} .brown{color:var(--brown)} .clay{color:#9a6448}
.partner{font-size:11px;font-weight:600;color:#8a8a8a}
.market{font-size:8px;display:flex;align-items:center;gap:10px}
.market i{display:inline-block;width:16px;height:10px;background:var(--orange)}
.footer{left:0;top:803px;width:678px;height:72px;background:var(--grey)}
.footer-item{top:836px;font-size:8px;font-weight:700}
.brand{left:48px;top:818px;display:flex;align-items:center;gap:6px;font-size:9px;font-weight:600;color:var(--gold)}
.brand i{width:32px;height:32px;border-radius:50%;background:var(--gold);display:block}
</style>
</head>
<body>

<section class="page page--talking">
  <h1 class="abs doc-title">EPS Talking Points</h1>
  <div class="abs title-rule"></div>
  <p class="abs intro">Polystyrene bans, recycling, and human health are top objections facing the EPS industry. When confronted with false allegations about EPS, here are some fast facts to help respond proactively. Perfect for packaging conferences, social media, and sales objectives.</p>
  <h2 class="abs section-head">Polystyrene Defense Line</h2>
  <p class="abs copy" style="left:37px;top:160px;width:293px"><b>Making Your Point</b> — Speaking with confidence means knowing your material. When responding to misstatements be prepared to challenge the source with factual information. Using a question format is less confrontational, e.g., “Did you know…” or “Were you aware…”? Make affirmative statements whenever possible; avoid restating the misinformation in your response. When addressing someone that refuses to give reasonable consideration to new information, we recommend responding, “It’s unfortunate you’re not willing to look into this further.” When given the opportunity to address an individual or an audience about EPS sustainability, focus on three (3) specific talking points to keep the discussion or presentation focused. Plan your talking points and don’t deviate; this is an effective strategy for dealing with media inquiries as well.</p>
  <svg class="abs" style="left:385px;top:132px" width="210" height="115" viewBox="0 0 210 115" aria-hidden="true">
    <ellipse cx="70" cy="55" rx="68" ry="48" fill="var(--blue)"/>
    <path d="M40 90 L30 113 L70 98Z" fill="var(--blue)"/>
    <ellipse cx="130" cy="43" rx="50" ry="38" fill="var(--orange)"/>
    <path d="M150 70 L190 96 L165 62Z" fill="var(--orange)"/>
  </svg>
  <p class="abs copy" style="left:367px;top:272px;width:275px"><b>Have a Bigger Voice</b> —The more educated we are, the more educated others will be. Share this document with your employees even if they do not deal directly with your customers or specific packaging audiences. Everyone working within the EPS industry should be aware of the strong environmental profile for EPS.</p>

  <div class="abs unit-bar" style="top:399px"><small>Information Unit #1</small><span>RECYCLING</span></div>

  <!-- Recyclable -->
  <div class="abs frame" style="left:30px;top:446px;width:228px;height:125px;border-color:var(--olive)"></div>
  <div class="abs" style="left:257px;top:446px;width:1px;height:234px;background:var(--olive)"></div>
  <div class="abs col-title olive" style="left:85px;top:437px">EPS is Recyclable</div>
  <svg class="abs" style="left:99px;top:461px" width="86" height="86" viewBox="0 0 86 86" aria-hidden="true">
    <circle cx="43" cy="43" r="43" fill="var(--olive)"/>
    <g fill="none" stroke="#fff" stroke-width="6" stroke-linejoin="round">
      <path d="M36 28 L43 20 L52 34"/><path d="M60 46 L64 56 L48 58"/><path d="M32 60 L22 56 L30 42"/>
    </g>
    <g fill="#fff"><path d="M48 36 L58 32 L56 42Z"/><path d="M44 52 L52 62 L42 64Z"/><path d="M26 40 L34 32 L36 44Z"/></g>
  </svg>
  <p class="abs fine" style="left:46px;top:562px;width:210px">Historically, EPS recycling averages <span class="olive big">~18%</span><br>&nbsp;&nbsp;&nbsp;&nbsp;&nbsp;&nbsp;&nbsp;&nbsp;over a <span class="olive big">25-year</span> trendline.</p>
  <div class="abs flat" role="img" aria-label="Stacked foam blocks icon" style="left:52px;top:607px;width:34px;height:22px;background:var(--olive)"></div>
  <p class="abs fine" style="left:93px;top:604px;width:150px">EPS recycling is most successful in commercial waste streams with large volume sources of EPS waste.</p>
  <p class="abs fine" style="left:45px;top:654px;width:140px;text-align:right">Consumer access to EPS recycling sometimes requires extra effort, but with proper equipment &amp; handling, it is successful in many communities.</p>
  <div class="abs flat" role="img" aria-label="Group of community members icon" style="left:195px;top:652px;width:42px;height:48px;background:var(--olive)"></div>
  <div class="abs partner" style="left:45px;top:730px">Crestmart</div>
  <div class="abs partner" style="left:123px;top:730px">Nutriwell</div>
  <div class="abs partner" style="left:210px;top:735px">Brightway</div>
  <div class="abs partner" style="left:45px;top:750px">Prairie Steaks</div>
  <div class="abs partner" style="left:150px;top:750px">Homeline</div>
  <div class="abs partner" style="left:100px;top:770px;font-size:9px">Harlow &amp; Finch</div>
  <p class="abs fine" style="left:45px;top:798px;width:212px;text-align:center">Creative problem solving for challenging recycling scenarios means Crestmart, Nutriwell, Harlow &amp; Finch, Homeline, Brightway, Prairie Steaks are committed to long term EPS recycling.</p>

  <!-- Technologies -->
  <div class="abs frame" style="left:282px;top:446px;width:160px;height:350px;border-color:var(--blue)"></div>
  <div class="abs col-title blue" style="left:287px;top:441px;width:130px">New EPS Recycling Technologies Are Emerging</div>
  <svg class="abs" style="left:309px;top:512px" width="86" height="86" viewBox="0 0 86 86" aria-hidden="true">
    <circle cx="43" cy="43" r="43" fill="var(--blue)"/>
    <path d="M43 22 a14 14 0 0 1 8 25 v6 h-16 v-6 a14 14 0 0 1 8-25Z" fill="none" stroke="#fff" stroke-width="3"/>
    <rect x="36" y="56" width="14" height="3" fill="#fff"/><rect x="37" y="61" width="12" height="3" fill="#fff"/>
    <path d="M24 20 l5 5 M62 20 l-5 5 M43 12 v5 M18 40 h5 M63 40 h5" stroke="#fff" stroke-width="2"/>
  </svg>
  <div class="abs flat" role="img" aria-label="Reprocessing machinery icon" style="left:322px;top:625px;width:46px;height:30px;background:var(--blue)"></div>
  <p class="abs fine" style="left:311px;top:667px;width:100px">Pyrolysis<br>—a chemical reprocessing method—increases the ability to recycle contaminated EPS waste.</p>
  <div class="abs flat" role="img" aria-label="Recycling facility buildings icon" style="left:316px;top:752px;width:72px;height:42px;background:var(--blue)"></div>
  <p class="abs fine" style="left:311px;top:811px;width:100px">Two new facilities opened in 2018.</p>

  <!-- End markets -->
  <div class="abs frame" style="left:445px;top:455px;width:190px;height:370px;border-color:var(--orange)"></div>
  <div class="abs col-title orange" style="left:465px;top:447px;width:146px">EPS End-Markets Show Consistent Growth</div>
  <svg class="abs" style="left:495px;top:512px" width="86" height="86" viewBox="0 0 86 86" aria-hidden="true">
    <circle cx="43" cy="43" r="43" fill="var(--orange)"/>
    <g fill="#fff"><rect x="20" y="50" width="8" height="12"/><rect x="31" y="42" width="8" height="20"/><rect x="42" y="34" width="8" height="28"/><rect x="53" y="26" width="8" height="36"/></g>
  </svg>
  <p class="abs fine" style="left:470px;top:620px;width:180px">It is used as recycled content in new EPS packaging and other EPS products.</p>
  <div class="abs flat" role="img" aria-label="Foam packaging pieces and box icon" style="left:486px;top:660px;width:104px;height:30px;background:var(--orange)"></div>
  <p class="abs fine" style="left:459px;top:718px">Markets for recycled content EPS include:</p>
  <div class="abs market" style="left:482px;top:742px"><i></i>Crown Molding</div>
  <div class="abs market" style="left:482px;top:765px"><i></i>Surfboards</div>
  <div class="abs market" style="left:482px;top:788px"><i></i>Picture Frames</div>
  <div class="abs market" style="left:482px;top:811px"><i></i>Other Rigid Polystyrene<br>Applications</div>
</section>

<section class="page page--units">
  <div class="abs unit-bar" style="top:27px"><small>Information Unit #2</small><span>EPS BANS</span></div>

  <div class="abs frame" style="left:40px;top:75px;width:215px;height:280px;border-color:var(--brown)"></div>
  <div class="abs col-title brown" style="left:52px;top:67px">Material Substitutions Are Risky</div>
  <svg class="abs" style="left:100px;top:92px" width="86" height="86" viewBox="0 0 86 86" aria-hidden="true">
    <circle cx="43" cy="43" r="43" fill="var(--brown)"/>
    <path d="M43 22 L64 58 H22Z" fill="none" stroke="#fff" stroke-width="4" stroke-linejoin="round"/>
    <rect x="41" y="34" width="4" height="13" fill="#fff"/><circle cx="43" cy="52" r="2.5" fill="#fff"/>
  </svg>
  <div class="abs flat" role="img" aria-label="Heavy weight icon" style="left:68px;top:205px;width:20px;height:34px;background:var(--brown)"></div>
  <p class="abs fine" style="left:105px;top:196px;width:130px">Recent studies show that heavier alternatives to lightweight plastics can significantly increase raw material requirements, energy consumption &amp; landfill volume.</p>
  <div class="abs flat" role="img" aria-label="Stack of banknotes icon" style="left:50px;top:285px;width:45px;height:30px;background:var(--brown)"></div>
  <p class="abs fine" style="left:105px;top:276px;width:135px">On a global scale, environmental costing indicates that plastics alternatives may cost $400 to $500 billion more<br><span class="brown" style="font-size:12px;font-weight:600">(4 to 5 times more).</span></p>
  <div class="abs flat" role="img" aria-label="Meat and fish icon" style="left:60px;top:338px;width:36px;height:42px;background:var(--brown)"></div>
  <p class="abs fine" style="left:105px;top:349px;width:140px">Meat, fish &amp; produce shipped in EPS have a longer shelf life, leading to less food waste.</p>

  <div class="abs frame" style="left:272px;top:75px;width:180px;height:270px;border-color:var(--olive)"></div>
  <div class="abs col-title olive" style="left:282px;top:67px;width:140px">EPS Is More Sustainable Than Most People Imagine</div>
  <svg class="abs" style="left:300px;top:109px" width="86" height="86" viewBox="0 0 86 86" aria-hidden="true">
    <circle cx="43" cy="43" r="43" fill="var(--olive)"/>
    <path d="M36 62 C26 44 38 26 56 22 C60 42 52 58 36 62Z" fill="#fff"/>
    <path d="M34 66 L48 34" stroke="var(--olive)" stroke-width="2.5"/>
  </svg>
  <div class="abs flat" role="img" aria-label="Moving air icon" style="left:342px;top:207px;width:40px;height:26px;background:var(--olive)"></div>
  <p class="abs fine" style="left:298px;top:248px;width:150px">EPS foam is of <span class="olive big">98% air</span>, which results in lower energy consumption.</p>
  <div class="abs flat" role="img" aria-label="Balance scale tipping toward EPS" style="left:316px;top:295px;width:80px;height:24px;background:var(--olive)"></div>
  <p class="abs fine" style="left:298px;top:334px;width:140px">Life cycle analyses show that EPS has far less impact on the environment than other competitive materials for the same use; in particular paper.</p>

  <div class="abs frame" style="left:468px;top:75px;width:175px;height:245px;border-color:var(--gold)"></div>
  <div class="abs col-title gold" style="left:472px;top:67px;width:160px">Litter Problems Are Not Material Dependent</div>
  <svg class="abs" style="left:507px;top:109px" width="86" height="86" viewBox="0 0 86 86" aria-hidden="true">
    <circle cx="43" cy="43" r="43" fill="var(--gold)"/>
    <path d="M28 36 L32 62 H54 L58 36" fill="none" stroke="#fff" stroke-width="4"/>
    <g fill="#fff"><rect x="38" y="22" width="5" height="5"/><rect x="48" y="16" width="4" height="4"/><rect x="44" y="44" width="5" height="5"/><rect x="60" y="58" width="5" height="5"/></g>
  </svg>
  <div class="abs flat" role="img" aria-label="Scattered litter pieces" style="left:497px;top:218px;width:85px;height:16px;background:var(--gold)"></div>
  <p class="abs fine" style="left:487px;top:244px;width:125px">A litter audit in San Francisco confirmed that a food service ban on polystyrene foam only changed the type of litter but did not reduce it.</p>
  <div class="abs flat" role="img" aria-label="Bins and improper disposal scene" style="left:505px;top:295px;width:90px;height:36px;background:var(--gold)"></div>
  <p class="abs fine" style="left:487px;top:342px;width:125px">Improper disposal of any material contributes to litter, whether it is EPS or another material.</p>

  <div class="abs unit-bar" style="top:404px"><small>Information Unit #3</small><span>HUMAN HEALTH &amp; SAFETY</span></div>

  <div class="abs frame" style="left:40px;top:452px;width:190px;height:275px;border-color:var(--clay)"></div>
  <div class="abs col-title clay" style="left:60px;top:445px;width:160px">There Is Very Little Residual Styrene in EPS.</div>
  <svg class="abs" style="left:97px;top:487px" width="86" height="86" viewBox="0 0 86 86" aria-hidden="true">
    <circle cx="43" cy="43" r="43" fill="var(--clay)"/>
    <path d="M30 44 l9 5 v10 l-9 5 l-9-5 v-10Z" fill="none" stroke="#fff" stroke-width="3"/>
    <path d="M50 20 v36 M42 48 l8 10 l8-10" fill="none" stroke="#fff" stroke-width="4"/>
  </svg>
  <div class="abs flat" role="img" aria-label="Strawberry and coffee mug icons" style="left:95px;top:583px;width:68px;height:30px;background:var(--clay)"></div>
  <p class="abs fine" style="left:72px;top:621px;width:150px">The amount of styrene that might exist in finished polystyrene is extremely small —often lower than naturally occurring styrene found in everyday food items like coffee, strawberries, and cinnamon.</p>
  <svg class="abs" style="left:92px;top:710px" width="76" height="22" viewBox="0 0 76 22" aria-hidden="true">
    <g fill="none" stroke="var(--clay)" stroke-width="2.5">
      <rect x="2" y="2" width="18" height="18"/><rect x="29" y="2" width="18" height="18"/><rect x="56" y="2" width="18" height="18"/>
      <path d="M6 10 l4 5 l8-10 M33 10 l4 5 l8-10 M60 10 l4 5 l8-10"/>
    </g>
  </svg>
  <p class="abs fine" style="left:72px;top:742px;width:155px">All chemicals need to be assessed in terms of risk versus exposure. Risks can be zero, negligible or harmful.</p>

  <div class="abs frame" style="left:253px;top:452px;width:180px;height:260px;border-color:var(--orange)"></div>
  <div class="abs col-title orange" style="left:268px;top:445px">EPS Is An Organic Polymer</div>
  <svg class="abs" style="left:300px;top:487px" width="86" height="86" viewBox="0 0 86 86" aria-hidden="true">
    <circle cx="43" cy="43" r="43" fill="var(--orange)"/>
    <circle cx="43" cy="43" r="35" fill="none" stroke="#fff" stroke-width="2"/>
    <text x="43" y="48" text-anchor="middle" font-family="Barlow, sans-serif" font-weight="700" font-size="13" fill="#fff">ORGANIC</text>
  </svg>
  <div class="abs flat" role="img" aria-label="Polystyrene structural formula" style="left:318px;top:580px;width:52px;height:60px;background:#f3d9a0"></div>
  <p class="abs fine" style="left:290px;top:653px;width:120px">Polystyrene is an organic compound consisting of hydrogen and carbon.</p>
  <div class="abs flat" role="img" aria-label="Reaction sparkle icon" style="left:326px;top:692px;width:24px;height:24px;background:var(--orange);border-radius:50%"></div>
  <p class="abs fine" style="left:290px;top:718px;width:125px">Polystyrene is chemically very inert, being resistant to acids and bases but is easily dissolved by many chlorinated solvents, and many aromatic hydrocarbon solvents.</p>

  <div class="abs frame" style="left:455px;top:452px;width:188px;height:255px;border-color:var(--blue)"></div>
  <div class="abs col-title blue" style="left:512px;top:445px">EPS Is Safe</div>
  <svg class="abs" style="left:507px;top:490px" width="86" height="86" viewBox="0 0 86 86" aria-hidden="true">
    <circle cx="43" cy="43" r="43" fill="var(--blue)"/>
    <path d="M43 20 L62 26 V44 C62 56 54 63 43 68 C32 63 24 56 24 44 V26Z" fill="none" stroke="#fff" stroke-width="4"/>
  </svg>
  <svg class="abs" style="left:532px;top:600px" width="34" height="34" viewBox="0 0 34 34" aria-hidden="true">
    <circle cx="17" cy="17" r="16" fill="var(--blue)"/>
    <path d="M10 17 l5 5 l9-10" fill="none" stroke="#fff" stroke-width="3"/>
  </svg>
  <p class="abs fine" style="left:484px;top:643px;width:150px">Polystyrene foam is approved for food contact by the national food authority and other global regulatory agencies.</p>
  <div class="abs" role="img" aria-label="Marine research office mark placeholder" style="left:543px;top:686px;width:24px;height:24px;background:var(--blue);border-radius:50%"></div>
  <p class="abs fine" style="left:484px;top:720px;width:150px">According to the National Marine Research Office (NMRO), “although marine debris is a global issue, there are significant gaps in our understanding of the problem.</p>

  <div class="abs footer"></div>
  <svg class="abs" style="left:0;top:803px" width="200" height="72" viewBox="0 0 200 72" aria-hidden="true"><path d="M0 0 H185 L160 72 H0Z" fill="#fff"/></svg>
  <div class="abs brand"><i></i>Foam Packaging<br>Alliance</div>
  <div class="abs footer-item" style="left:197px">Foam Packaging Alliance</div>
  <div class="abs footer-item" style="left:333px">foamtradeunion.org</div>
  <div class="abs footer-item" style="left:447px">(800) 555-0142</div>
  <div class="abs footer-item" style="left:565px">copyright 2019</div>
</section>

</body>
</html>
```